Business Card Design for Marketing Firm

Looking for business card design for higher end marketing firm. Clean but impressionable/trendy. We are a marketing firm that represents manufacturers in the foodservice equipment and supply industry. Our customers are end users such has hotels, restaurants, country clubs, convention centers and casinos as well as distributors of restaurants supplies and equipment, and manufacturers of foodservice equipment and supplies.
Target Market(s)
Hotels, Restaurants, Supply & Equipment Distributors, Foodservice Manufacturers
Industry/Entity Type
Foodservice/Hospitality
Contact Information for Business Card
Name, Title, Contact Number, Email, Website, Social Media, Address
Requirements
Must have
- Clean & Simple but Serious and Impressionable

```html
<!DOCTYPE html>
<html lang="en">
<head>
<meta charset="utf-8">
<title>Meridian Hospitality Reps – Business Card</title>
<link rel="stylesheet" href="https://fonts.googleapis.com/css2?family=Montserrat:wght@400;500;700&display=swap">
<style>
  :root {
    --backdrop: #e4e6e9;
    --indigo: #3b3c86;
    --indigo-deep: #2e2f6d;
    --indigo-light: #4a4b94;
    --band: #4c50a4;
    --card-white: #ffffff;
    --ink: #1d1d22;
    --ink-soft: #2a2a30;
  }
  * { box-sizing: border-box; margin: 0; padding: 0; }
  html, body {
    width: 1200px; height: 1200px; overflow: hidden;
    background: var(--backdrop);
    font-family: "Montserrat", Arial, sans-serif;
  }
  .canvas { position: relative; width: 1200px; height: 1200px; }

  .card { position: absolute; left: 214px; width: 760px; height: 434px; overflow: hidden; }

  /* Front */
  .card-front { top: 120px; background: var(--indigo); }
  .front-pattern {
    position: absolute; inset: 0;
    background: linear-gradient(160deg, var(--indigo-light) 0%, var(--indigo) 50%, var(--indigo-deep) 100%);
  }
  .front-brand {
    position: absolute; left: 0; right: 0; top: 240px;
    text-align: center; color: var(--card-white);
    font-weight: 500; font-size: 30px; letter-spacing: 1px; line-height: 1.3;
  }

  /* Back */
  .card-back { top: 642px; background: var(--card-white); }
  .back-brand {
    position: absolute; right: 52px; top: 108px; width: 220px;
    text-align: right; color: var(--indigo);
    font-weight: 500; font-size: 15px; letter-spacing: .5px; line-height: 1.3;
  }
  .holder { position: absolute; left: 54px; top: 250px; }
  .holder-name { font-size: 34px; font-weight: 700; color: var(--ink); letter-spacing: .3px; }
  .holder-title { font-size: 16px; font-weight: 400; color: var(--ink-soft); margin-top: 2px; }

  .contact-list { position: absolute; left: 437px; top: 172px; list-style: none; }
  .contact-item {
    display: flex; align-items: center; gap: 14px;
    height: 36px; font-size: 18px; font-weight: 500; color: var(--ink);
  }
  .contact-icon {
    width: 27px; height: 27px; border-radius: 50%;
    background: var(--indigo); display: flex; align-items: center; justify-content: center;
  }
  .contact-icon svg { width: 15px; height: 15px; }

  .social-band {
    position: absolute; left: 8px; right: 8px; top: 347px; height: 31px;
    background: linear-gradient(90deg, rgba(76,80,164,0) 0%, var(--band) 23%, var(--band) 77%, rgba(76,80,164,0) 100%);
    display: flex; justify-content: center; align-items: center; gap: 38px;
    color: var(--card-white); font-size: 15px; font-weight: 400;
  }
  .social-item { display: flex; align-items: center; gap: 7px; }
  .social-dot { width: 12px; height: 12px; border: 1.5px solid var(--card-white); border-radius: 50%; }
</style>
</head>
<body>
<main class="canvas">

  <section class="card card-front">
    <div class="front-pattern" role="img" aria-label="Layered indigo chevron pattern background"></div>
    <div class="front-brand">MERIDIAN HOSPITALITY REPS</div>
  </section>

  <section class="card card-back">
    <div class="back-brand">MERIDIAN HOSPITALITY REPS</div>

    <div class="holder">
      <h1 class="holder-name">YOUR NAME</h1>
      <p class="holder-title">Title here</p>
    </div>

    <ul class="contact-list">
      <li class="contact-item">
        <span class="contact-icon">
          <svg viewBox="0 0 16 16"><path fill="#fff" d="M3.5 1.5l2.2 2.6-1.2 1.6c.9 2 2.4 3.6 4.4 4.6l1.6-1.2 2.6 2.2-1.2 2.2C6.8 13.3 2.6 9.2 1.4 3.1z"/></svg>
        </span>000 123 456
      </li>
      <li class="contact-item">
        <span class="contact-icon">
          <svg viewBox="0 0 16 16"><rect x="2" y="4" width="12" height="8.5" rx="1" fill="#fff"/><path d="M2.5 4.8L8 9l5.5-4.2" stroke="#3b3c86" stroke-width="1.3" fill="none"/></svg>
        </span>your email here
      </li>
      <li class="contact-item">
        <span class="contact-icon">
          <svg viewBox="0 0 16 16" fill="none" stroke="#fff" stroke-width="1.3"><circle cx="8" cy="8" r="6"/><ellipse cx="8" cy="8" rx="2.6" ry="6"/><path d="M2 8h12M3 5h10M3 11h10"/></svg>
        </span>your website here
      </li>
      <li class="contact-item">
        <span class="contact-icon">
          <svg viewBox="0 0 16 16"><path fill="#fff" d="M8 1.5a4.6 4.6 0 0 1 4.6 4.6C12.6 9.5 8 14.5 8 14.5S3.4 9.5 3.4 6.1A4.6 4.6 0 0 1 8 1.5z"/><circle cx="8" cy="6.1" r="1.7" fill="#3b3c86"/></svg>
        </span>your location here
      </li>
    </ul>

    <div class="social-band">
      <span class="social-item"><span class="social-dot"></span>snapshare</span>
      <span class="social-item"><span class="social-dot"></span>friendpage</span>
    </div>
  </section>

</main>
</body>
</html>
```